WordPress Website Design for Multi-Brand Aviation Group (Unified Branding System)

Project Overview:
We are seeking a professional, modern WordPress website design for an aviation-focused umbrella company that owns and operates multiple subsidiary businesses. The goal is to create a cohesive visual system that clearly communicates that each company operates under the same parent organization, while still allowing each brand to maintain a slightly distinct identity.
This is not just a single website design—we are looking for a scalable design framework that can be applied across multiple aviation-related businesses.
Objectives:
- Establish a consistent, recognizable brand identity across all company websites
Clearly communicate the relationship between the parent company and its subsidiaries
-bCreate a clean, high-end corporate aviation aesthetic
- Ensure all designs are SEO-friendly and optimized for performance
- Allow flexibility for future expansion (additional subsidiaries)
- Target Audience:
- Corporate aviation clients
- Charter customers
- Students wishing to receive flight training
- Aircraft owners and operators
- Turbine aircraft training to meet insurance requirements
- Business professionals and high-net-worth individuals
- Aviation industry partners
Design Direction & Style:
We are looking for a premium, professional aviation feel—think clean, modern, and high-trust. The design should reflect the standards of corporate aviation: precision, safety, and sophistication.
Key style notes:
Minimalist but impactful layout
High-quality aviation photography (jets, interiors, operations, global travel)
Subtle motion/interaction (hover effects, transitions)
Clear typography hierarchy for readability and professionalism
Branding Requirements:
Incorporate the primary colors of the parent company logo across all designs
Website Structure (Core Pages):
Design a system that includes:
Home Page with the following links:
- About / Company Overview
- Aircraft Management
- Aircraft Acquisition
- Charter
- Pilot Services
- Trip Support
- Contact Page
Site should further include:
- Mobile-first responsive design
- Fast-loading, performance-optimized layouts
SEO & Technical Considerations:
- Design should support high-level SEO implementation:
- Clean layout structure that translates well to semantic HTML
- Proper heading hierarchy (H1, H2, H3)
- Space for keyword-rich content without clutter
- Optimized image placement (with alt text capability)
- Fast load times (lightweight design approach)
- Compatibility with WordPress SEO plugins (e.g., Yoast or Rank Math)
WordPress Requirements:
- Design should be easily built using WordPress (preferred builders: Elementor, Gutenberg, or similar)
- Reusable templates for scalability across multiple sites
- Easy for non-developers to update text and images
- Modular components (blocks/sections that can be reused across pages and sites)
- Navigation & UX:
- Simple, intuitive navigation
- Sticky header preferred
Style guide including:
- Colors
- Fonts
- Button styles
- Layout system
- Designs similar to high-end corporate aviation, private jet charter, or luxury service brands are preferred—clean, sharp, and premium without being overly flashy.
What We Want to Avoid:
- Overly busy layouts
- Generic templates with no brand identity
- Outdated or “stock” looking aviation designs
- Poor mobile responsiveness
Additional Notes:
We are building a long-term brand system, not just a one-off website. There is potential for ongoing work as we expand additional subsidiary sites.
We value designers who understand branding consistency across multiple business units and can create a scalable, professional system.
Include the attached main company logo "Tarnwell Aviation Group" and the "Member FLTC" logo on the main page.
1 page

```html
<!DOCTYPE html>
<html lang="en">
<head>
<meta charset="utf-8">
<title>Tarnwell Aviation Group</title>
<link rel="stylesheet" href="https://fonts.googleapis.com/css2?family=Archivo:wght@400;500;600&family=Montserrat:wght@400;500;600;700&display=swap">
<style>
:root{
  --blue:#0b5cb8;
  --blue-dark:#084a97;
  --blue-soft:#9fc0e6;
  --yellow:#f7c600;
  --ink:#141414;
  --muted:#5c5c5c;
  --line:#d6dde6;
  --white:#ffffff;
  --pill:#f1f1f1;
}
*{box-sizing:border-box;margin:0;padding:0}
html,body{width:1200px;height:4948px;overflow:hidden;background:var(--white)}
body{position:relative;font-family:"Montserrat",sans-serif;color:var(--ink)}
.abs{position:absolute}
h1,h2,h3,.display{font-family:"Archivo",sans-serif;font-weight:500;text-transform:uppercase;line-height:1}
a{color:inherit;text-decoration:none}

/* buttons */
.btn{display:inline-flex;align-items:center;height:34px;background:var(--yellow);border-radius:17px;padding-left:26px;font-size:10px;font-weight:700;text-transform:uppercase;color:var(--ink);white-space:nowrap}
.btn .go{width:30px;height:30px;border-radius:50%;background:var(--yellow);border:3px solid var(--white);margin-left:22px;margin-right:-12px;display:flex;align-items:center;justify-content:center}
.btn .go svg{width:12px;height:12px}
.tag{display:inline-block;height:28px;line-height:26px;padding:0 24px;border:1px solid #cfcfcf;border-radius:14px;background:var(--pill);font-size:11px;color:#8d8d8d;text-transform:uppercase;font-weight:500}
.tag.on-blue{background:#e9eef5;color:#8a97a8;border-color:#e9eef5}

/* header */
.site-header{left:15px;top:15px;width:1170px;height:66px;border:3px solid var(--blue);border-radius:33px;background:var(--white);display:flex;align-items:center;padding:0 34px;z-index:3}
.brand{display:flex;flex-direction:column;line-height:1}
.brand .name{font-family:"Archivo",sans-serif;font-size:20px;font-weight:600;color:var(--blue);letter-spacing:1px}
.brand .sub{font-family:"Archivo",sans-serif;font-size:8px;font-weight:600;color:var(--blue);letter-spacing:1.2px;margin-top:2px}
.main-nav{display:flex;gap:20px;margin-left:98px;font-size:10px;text-transform:uppercase;color:var(--blue)}
.header-end{margin-left:auto;display:flex;gap:30px;font-size:10px;color:var(--blue)}
.header-end .contact{border-bottom:1px solid var(--blue);padding-bottom:3px}

/* hero */
.hero{left:19px;top:100px;width:1162px;height:574px;border-radius:20px;overflow:hidden;background:linear-gradient(180deg,#3f6fa8 0%,#8fb0d6 35%,#5f89bd 60%,#1650a0 100%)}
.hero-copy{left:0;top:312px;width:1162px;text-align:center;color:var(--white)}
.hero-copy h1{font-size:48px;letter-spacing:1px;line-height:.92}
.hero-copy p{font-size:11px;line-height:18px;width:580px;margin:22px auto 0}
.hero-copy .btn{margin-top:20px}
.member-notch{left:989px;top:576px;width:196px;height:104px;background:var(--white);border-top-left-radius:28px;display:flex;flex-direction:column;justify-content:center;padding-left:18px}
.member-notch .lbl{font-size:8px;color:var(--ink);margin-left:40px}
.member-notch .mark{display:flex;align-items:center;gap:10px;margin-top:2px}
.member-notch .dot{width:36px;height:36px;border-radius:50%;background:var(--blue)}
.member-notch .mark span{font-family:"Archivo",sans-serif;font-size:28px;font-weight:500;color:var(--ink);letter-spacing:2px}

/* services */
.section-head{left:0;width:1200px;text-align:center}
.section-head h2{font-size:50px;margin-top:22px}
.section-head p{font-size:11px;line-height:18px;width:660px;margin:20px auto 0;color:#333}
.service-card{width:246px;height:346px;border:1.5px solid var(--blue-soft);border-radius:16px;text-align:center;padding:11px}
.service-card .photo{height:217px;border-radius:10px}
.service-card h3{font-size:22px;margin-top:28px;line-height:1.05;color:var(--ink)}
.arrow-dot{width:30px;height:30px;border-radius:50%;background:var(--yellow);border:3px solid var(--white);display:flex;align-items:center;justify-content:center}
.arrow-dot svg{width:11px;height:11px}
.service-card .arrow-dot{position:absolute;left:108px;bottom:-16px}

/* leaders */
.band{left:19px;width:1162px;background:var(--blue);border-radius:20px}
.leader-photo{width:316px;height:432px;border-radius:12px}
.leader-card{left:442px;top:1549px;width:316px;height:432px;background:var(--white);border-radius:14px;text-align:center;padding-top:52px}
.leader-card h2{font-size:48px;margin-top:22px;line-height:.98}
.leader-card p{font-size:10.5px;line-height:17.5px;width:250px;margin:20px auto 0;color:#333}
.leader-card .btn{margin-top:16px}
.stats{left:106px;top:2003px;width:988px;height:147px;background:var(--white);border-radius:14px;display:flex;align-items:center}
.stat{flex:1;text-align:center;position:relative}
.stat + .stat::before{content:"";position:absolute;left:0;top:10px;width:1px;height:58px;background:#c9c9c9}
.stat strong{display:block;font-family:"Archivo",sans-serif;font-weight:500;font-size:44px;color:var(--blue)}
.stat span{display:block;font-size:11px;line-height:16px;color:#555;margin-top:10px}

/* priority */
.priority-head{left:213px;top:2327px;width:800px}
.priority-head h2{font-size:46px;margin-top:16px;line-height:.98;color:var(--ink)}
.priority-head p{font-size:11px;line-height:18px;width:600px;margin-top:30px;color:#333}
.feature-card{width:246px;height:359px;border-radius:14px;overflow:hidden}
.feature-card h3{position:absolute;left:32px;bottom:28px;color:var(--white);font-size:23px;line-height:.96}

/* testimonials */
.quote-card{left:278px;top:3274px;width:644px;height:224px;background:var(--white);border-radius:8px;text-align:center;padding-top:26px}
.quote-card .marks{font-family:"Archivo",sans-serif;font-size:96px;line-height:60px;height:50px;color:var(--yellow);font-weight:600}
.quote-card p{font-size:11px;line-height:18px;width:540px;margin:22px auto 0;color:#333}
.quote-card .who{font-size:11px;font-weight:700;margin-top:14px}
.quote-card .role{font-size:9px;color:#888;margin-top:2px}
.nav-arrow{width:30px;height:30px;border-radius:50%;background:var(--white);display:flex;align-items:center;justify-content:center}
.nav-arrow svg{width:14px;height:14px}

/* faq */
.faq-head{left:213px;top:3757px}
.faq-head h2{font-size:46px;margin-top:16px;line-height:.98}
.faq-item{left:213px;width:509px;border:1.5px solid var(--blue-soft);border-radius:6px;padding:0 16px 0 18px}
.faq-item .q{display:flex;align-items:center;height:40px;font-size:11px;font-weight:600}
.faq-item .q .num{margin-right:12px}
.faq-item .toggle{margin-left:auto;width:26px;height:26px;border-radius:4px;background:var(--blue);color:var(--white);display:flex;align-items:center;justify-content:center;font-size:16px;font-weight:500}
.faq-item .a{font-size:9.5px;line-height:13px;color:#555;padding:10px 80px 16px 30px}

/* footer */
.footer-brand{left:213px;top:4460px}
.footer-brand .name{font-family:"Archivo",sans-serif;font-size:30px;font-weight:600;color:var(--white);letter-spacing:1.5px;line-height:1}
.footer-brand .sub{font-family:"Archivo",sans-serif;font-size:12px;font-weight:600;color:var(--white);letter-spacing:1.8px;margin-top:2px}
.socials{left:213px;top:4548px;display:flex;gap:20px}
.socials span{width:28px;height:28px;border-radius:50%;border:1.5px solid var(--white)}
.copyright{left:213px;top:4618px;font-size:9.5px;line-height:12px;color:var(--white)}
.footer-col{top:4492px;color:var(--white)}
.footer-col h4{font-size:12px;font-weight:600;margin-bottom:18px}
.footer-col li{list-style:none;font-size:10px;line-height:24px}
.footer-rule{left:213px;top:4700px;width:774px;height:1px;background:rgba(255,255,255,.35)}
.departure{left:213px;top:4762px;color:var(--white);font-size:34px;line-height:.98}
.departure-note{left:678px;top:4748px;width:300px;font-size:10px;line-height:17px;color:var(--white)}
.to-top{left:1068px;top:4867px;width:50px;height:50px;border-radius:50%;background:var(--yellow);border:4px solid var(--white);display:flex;align-items:center;justify-content:center}
.legal{left:213px;top:4910px;font-size:10px;color:#333}
</style>
</head>
<body>

<svg width="0" height="0" style="position:absolute">
  <defs>
    <symbol id="ne" viewBox="0 0 12 12"><path d="M3 9 9 3M4 3h5v5" fill="none" stroke="#141414" stroke-width="1.4" stroke-linecap="round"/></symbol>
  </defs>
</svg>

<header class="abs site-header">
  <div class="brand"><span class="name">TARNWELL</span><span class="sub">AVIATION GROUP</span></div>
  <nav class="main-nav">
    <a>Home</a><a>About</a><a>Aircraft Management</a><a>Aircraft Acquisition</a><a>Charter</a><a>Pilot Services</a><a>Trip Support</a>
  </nav>
  <div class="header-end"><a class="contact">CONTACT US ↗</a><a>ENG ▾</a></div>
</header>

<section class="abs hero" role="img" aria-label="Passenger jet climbing overhead against a blue sky with white clouds"></section>
<div class="abs hero-copy">
  <h1>Driving Global Aviation<br>Excellence</h1>
  <p>Lorem Ipsum is simply dummy text of the printing and typesetting industry. Lorem Ipsum has been the industry's standard dummy text ever since the 1500s.</p>
  <a class="btn">Get a Quote<span class="go"><svg><use href="#ne"/></svg></span></a>
</div>
<div class="abs member-notch">
  <span class="lbl">member of</span>
  <div class="mark"><span class="dot"></span><span>FLTC</span></div>
</div>

<section class="abs section-head" style="top:764px">
  <span class="tag">Services</span>
  <h2>Our Aviation Solutions</h2>
  <p>Lorem Ipsum is simply dummy text of the printing and typesetting industry. Lorem Ipsum has been the industry's standard dummy text ever since the 1500s.</p>
</section>
<article class="abs service-card" style="left:213px;top:933px">
  <div class="photo" role="img" aria-label="Flight operations control room with large screens" style="background:linear-gradient(160deg,#6f8fb5,#2c3f5c 60%,#4a3428)"></div>
  <h3>Aircraft<br>Management</h3>
  <span class="arrow-dot"><svg><use href="#ne"/></svg></span>
</article>
<article class="abs service-card" style="left:476px;top:933px">
  <div class="photo" role="img" aria-label="Technician inspecting a small propeller aircraft in a hangar" style="background:linear-gradient(160deg,#8e9aa6,#dfe3e6 50%,#5d6a78)"></div>
  <h3>Aircraft<br>Acquisition</h3>
  <span class="arrow-dot"><svg><use href="#ne"/></svg></span>
</article>
<article class="abs service-card" style="left:741px;top:933px">
  <div class="photo" role="img" aria-label="Flight instructor with a student in a cockpit" style="background:linear-gradient(160deg,#9cc3e6,#5b7fa3 50%,#2a3a4e)"></div>
  <h3>Flight<br>Training</h3>
  <span class="arrow-dot"><svg><use href="#ne"/></svg></span>
</article>
<div class="abs" style="left:520px;top:1340px"><a class="btn">View All<span class="go"><svg><use href="#ne"/></svg></span></a></div>

<section class="abs band" style="top:1463px;height:776px"></section>
<div class="abs leader-photo" style="left:106px;top:1549px;background:linear-gradient(170deg,#c9d3dc,#8a98a6 55%,#3b3f46)" role="img" aria-label="Airline captain in uniform standing beside an aircraft"></div>
<article class="abs leader-card">
  <span class="tag">Trusted</span>
  <h2>Aviation<br>Leaders</h2>
  <p>Lorem Ipsum is simply dummy text of the printing and typesetting industry. Lorem Ipsum has been the industry's standard dummy text ever since the 1500s, when an unknown printer took a galley of type and scrambled it to make a type specimen book.</p>
  <a class="btn">Our Story &amp; Vision<span class="go"><svg><use href="#ne"/></svg></span></a>
</article>
<div class="abs leader-photo" style="left:778px;top:1549px;background:linear-gradient(170deg,#d7dde3,#7c8fa6 55%,#2f3b4d)" role="img" aria-label="Two business travellers with luggage in an airport terminal"></div>
<div class="abs stats">
  <div class="stat"><strong>20+</strong><span>Years of Aviation<br>Excellence</span></div>
  <div class="stat"><strong>99.9%</strong><span>Seamless Flight<br>Operations</span></div>
  <div class="stat"><strong>24/7</strong><span>Global Mission<br>Support</span></div>
</div>

<section class="abs priority-head">
  <span class="tag">Priority</span>
  <h2>Where Precision Meets The<br>Highest Standard</h2>
  <p>Lorem Ipsum is simply dummy text of the printing and typesetting industry. Lorem Ipsum has been the industry's standard dummy text ever since the 1500s.</p>
</section>
<article class="abs feature-card" style="left:213px;top:2563px;background:linear-gradient(180deg,#a9b6c4 0%,#6f829a 45%,#0b5cb8 100%)" role="img" aria-label="Row of airliners lined up on an airport apron">
  <h3>Global<br>Standards<br>Alignment</h3>
</article>
<article class="abs feature-card" style="left:476px;top:2563px;background:linear-gradient(180deg,#c3ccd6 0%,#7d8a99 40%,#0b5cb8 100%)" role="img" aria-label="Ground engineer in high-visibility gear checking a jet engine">
  <h3>Safety &amp;<br>Performance<br>Focus</h3>
</article>
<article class="abs feature-card" style="left:741px;top:2563px;background:linear-gradient(180deg,#dfe6ee 0%,#8ea6c2 45%,#0b5cb8 100%)" role="img" aria-label="Technical blueprint-style rendering of an aircraft">
  <h3>Scalable<br>Operational<br>Design</h3>
</article>

<section class="abs band" style="top:3011px;height:656px"></section>
<div class="abs section-head" style="top:3101px;color:var(--white)">
  <span class="tag on-blue">Testimonials</span>
  <h2 style="font-size:46px;line-height:.98;margin-top:14px">Voices of<br>Industry Trust</h2>
</div>
<span class="abs nav-arrow" style="left:228px;top:3370px"><svg viewBox="0 0 14 14"><path d="M11 7H3M6 4 3 7l3 3" fill="none" stroke="#0b5cb8" stroke-width="1.6" stroke-linecap="round"/></svg></span>
<span class="abs nav-arrow" style="left:940px;top:3370px"><svg viewBox="0 0 14 14"><path d="M3 7h8M8 4l3 3-3 3" fill="none" stroke="#0b5cb8" stroke-width="1.6" stroke-linecap="round"/></svg></span>
<article class="abs quote-card">
  <div class="marks">”</div>
  <p>Lorem Ipsum is simply dummy text of the printing and typesetting industry. Lorem Ipsum has been the industry's standard dummy text ever since the 1500s, when an unknown printer took a galley of type and scrambled it to make a type specimen book.</p>
  <div class="who">Daniel Reed.</div>
  <div class="role">Lorem Ipsum</div>
</article>
<div class="abs" style="left:490px;top:3544px"><a class="btn">Get a Consultation<span class="go"><svg><use href="#ne"/></svg></span></a></div>

<section class="abs faq-head">
  <span class="tag">Need Help</span>
  <h2>Frequently Asked<br>Questions</h2>
</section>
<div class="abs faq-item" style="top:3928px"><div class="q"><span class="num">01.</span>Lorem Ipsum is simply dummy text of the printing?<span class="toggle">+</span></div></div>
<div class="abs faq-item" style="top:3984px;height:136px"><div class="q"><span class="num">02.</span>Lorem Ipsum is simply dummy text?<span class="toggle">×</span></div>
  <div class="a">Lorem Ipsum is simply dummy text of the printing and typesetting industry. Lorem Ipsum has been the industry's standard dummy text ever since the 1500s, when an unknown printer took a galley of type and scrambled it to make a type specimen book.</div></div>
<div class="abs faq-item" style="top:4134px"><div class="q"><span class="num">03.</span>Lorem Ipsum is simply dummy text of the printing?<span class="toggle">+</span></div></div>
<div class="abs faq-item" style="top:4191px"><div class="q"><span class="num">04.</span>Lorem Ipsum is simply dummy text?<span class="toggle">+</span></div></div>
<div class="abs faq-item" style="top:4247px"><div class="q"><span class="num">05.</span>Lorem Ipsum is simply dummy text of the printing?<span class="toggle">+</span></div></div>
<div class="abs" style="left:741px;top:3928px;width:246px;height:361px;border-radius:12px;background:linear-gradient(180deg,#c4d2df 0%,#e6dccb 60%,#d2b48e 100%)" role="img" aria-label="Jet airliner approaching head-on with landing gear down"></div>

<footer class="abs band" style="top:4378px;height:512px"></footer>
<div class="abs footer-brand"><div class="name">TARNWELL</div><div class="sub">AVIATION GROUP</div></div>
<div class="abs socials"><span></span><span></span><span></span><span></span></div>
<p class="abs copyright">Copyright © 2026 TARNWELL<br>AVIATION GROUP.<br>All Rights Reserved.</p>
<div class="abs footer-col" style="left:493px"><h4>Explore</h4><ul><li>What We Offer</li><li>Case Studies</li><li>Blog &amp; Insights</li><li>Resources</li><li>FAQs</li></ul></div>
<div class="abs footer-col" style="left:678px"><h4>Company</h4><ul><li>Home</li><li>About</li><li>Service</li><li>Testimonials</li><li>FAQs</li></ul></div>
<div class="abs footer-col" style="left:864px"><h4>Legal Links</h4><ul><li>Privacy Policy</li><li>Cookie Policy</li><li>Disclaimer</li><li>Copyright</li></ul></div>
<div class="abs footer-rule"></div>
<h2 class="abs departure">Ready for<br>Departure?</h2>
<p class="abs departure-note">Lorem Ipsum is simply dummy text of the printing and typesetting industry.</p>
<div class="abs" style="left:676px;top:4804px"><a class="btn">Contact Us<span class="go"><svg><use href="#ne"/></svg></span></a></div>
<a class="abs to-top" aria-label="Back to top"><svg width="16" height="16" viewBox="0 0 16 16"><path d="M8 13V3M4 7l4-4 4 4" fill="none" stroke="#141414" stroke-width="1.8" stroke-linecap="round"/></svg></a>
<p class="abs legal">Privacy Policy &nbsp;|&nbsp; Terms &amp; Conditions</p>

</body>
</html>
```